A professional business to business web site for a contract agency called VONTAREX.

We need a very clean, very professional web site created for business to business. It is an informational web site with 3 pages. We are a company that offers contract employee placements into primarily the pharmaceutical industry. I have attached a file that describes the company more fully.

Hi,

I'm sorry if I wasn't clear, but I need to have the HTML pages created so I can just upload the files you give me to the web hosting site.

Please let me know if you have any questions.

Thanks for working on my project!

Hello,

I didn't put this in the description, but I would need the web site set up on the web hosting site as well.  The web hosting site is abrightkettle.  I want a copy of all the files as well.

Thanks,
Miles

Reason: I'm sorry, unexpectedly, I have been very busy and I haven't been able to devote the time necessary for this. I am extending the deadline by 10 days. Thank you for your patience. Thanks.

Reason: Hi everyone, I apologize again, but everything has been so busy here that I haven't been able to give this attention. I plan to work on this over the next few days. Thanks and sorry again, Miles.

Reason: I'm sorry this is taking longer than planned. I have been extremely busy. I have increased the budget on this project. Thanks.

Target Market(s)

Large professional corporations mainly in the pharmaceutical industry. The audience is hiring decisions makers within the companies and potential job candidates/job seekers.

Industry/Entity Type

Pharmaceutical

Font styles to use
Sans Serif

Requirements
Must have
• Must have a clean look that mimics the pharmaceutical industry web sites. VERY professional.
Nice to have
• A nice picture of professional business/pharma/technical people looking like a team. Colors are listed on the attached Word document.
Should not have
• No animation. Not too busy.

```html
<!DOCTYPE html>
<html lang="en">
<head>
<meta charset="utf-8">
<title>VONTAREX – Services</title>
<link href="https://fonts.googleapis.com/css2?family=Arimo:ital,wght@0,400;0,700;1,400&display=swap" rel="stylesheet">
<style>
:root{
  --navy:#13237f;
  --navy-text:#1a2b8c;
  --ink:#444;
  --muted:#7a7a7a;
  --rule:#dcdcdc;
  --band:#f2f2f2;
  --caption:#e8e8e8;
  --footer:#333333;
  --footer-text:#9a9a9a;
  --white:#fff;
}
*{margin:0;padding:0;box-sizing:border-box}
html,body{width:1200px;height:1047px;overflow:hidden;background:var(--white)}
body{position:relative;font-family:"Arimo",Arial,sans-serif;color:var(--ink)}
.abs{position:absolute}

.topbar{left:0;top:0;width:1200px;height:24px;background:var(--navy);color:var(--white);font-size:9px;font-weight:700}
.topbar .welcome{left:259px;top:7px}
.topbar .hotline{right:239px;top:7px}

.brand{left:259px;top:53px;display:flex;align-items:center;gap:10px}
.brand .dot{width:36px;height:36px;border-radius:50%;background:var(--navy)}
.brand .name{font-size:20px;letter-spacing:4px;color:var(--navy);font-weight:400}

.social-head{left:772px;top:70px;display:flex;gap:11px}
.social-head span{width:11px;height:11px;border-radius:2px;background:#9a9a9a}

.search{left:863px;top:64px;width:99px;height:24px;border:1px solid #e0e0e0;background:#f7f7f7;font-size:8px;color:#999;padding:7px 9px}
.search svg{position:absolute;right:6px;top:5px}

.nav{top:108px;font-size:9.5px;color:#555;left:259px;width:703px;height:12px}
.nav span{position:absolute;top:0}
.nav .active{color:var(--navy-text)}
.nav i{position:absolute;top:-1px;width:1px;height:12px;background:#ccc}

.titleband{left:0;top:128px;width:1200px;height:68px;background:var(--band)}
.titleband h1{position:absolute;left:259px;top:21px;font-size:14.5px;font-weight:400;color:#555}
.titleband .crumb{position:absolute;left:259px;top:43px;font-size:7.5px;color:#666}
.titleband .shade{position:absolute;left:259px;top:63px;width:703px;height:3px;background:linear-gradient(90deg,transparent,#bdbdbd 50%,transparent);border-radius:50%}

.side{left:259px;top:224px;width:127px;font-size:8px;font-weight:700;color:#666}
.side li{list-style:none;position:absolute;left:0;width:127px;line-height:10.5px}
.side .current{color:var(--navy-text)}
.side hr{position:absolute;left:0;width:127px;border:0;border-top:1px solid var(--rule)}

.intro{left:418px;top:223px;width:270px;font-size:7.6px;line-height:10.5px;color:var(--muted)}
.intro h2{font-size:9.5px;font-weight:400;color:var(--navy-text);margin-bottom:12px}
.intro p{margin-bottom:11px}
.intro b{color:#444;font-weight:400}

.feature-media{left:772px;top:232px;width:118px;height:98px;border-radius:40px;background:radial-gradient(circle at 40% 45%,#f0c08a,#d43a2a 45%,#c9c9c9 75%,transparent 76%)}

.divider{left:259px;top:389px;width:703px;height:1px;background:var(--rule)}

.card{width:229px;height:196px}
.card .media{height:156px}
.card .cap{height:40px;background:var(--caption);text-align:center;color:#555;padding-top:8px}
.card .cap h3{font-size:10.5px;font-weight:400;letter-spacing:.2px}
.card .cap p{font-size:7.5px;margin-top:4px}
.card.active .cap{background:var(--navy);color:var(--white)}
.m-screen{background:linear-gradient(135deg,#2a6fb0,#7fb6e0 45%,#3d5f86)}
.m-tube{background:radial-gradient(ellipse at 40% 50%,#c8c8c8 0,#6a6a6a 18%,#141414 45%,#0a0a0a)}
.m-caps{background:radial-gradient(circle at 55% 55%,#3fb0e0,#126a9a 45%,#050a10 85%)}

.pager{top:834px;height:23px;border:1px solid var(--rule);font-size:7.5px;color:#666;text-align:center;line-height:21px}

.footer{left:0;top:885px;width:1200px;height:162px;background:var(--footer)}
.footer .mark{position:absolute;left:262px;top:31px;width:38px;height:38px;border-radius:50%;background:#555}
.footer h4{position:absolute;font-size:8.5px;font-weight:400;color:#eee;letter-spacing:.2px}
.footer .uline{position:absolute;height:1px;background:#555}
.footer .about{position:absolute;left:259px;top:80px;width:295px;font-size:7.5px;line-height:10.5px;font-style:italic;color:var(--footer-text)}
.footer .about p{margin-bottom:10px}
.footer .office{position:absolute;left:611px;top:80px;font-size:7.5px;line-height:14.5px;color:#ccc}
.footer .office a{color:#3aa3e0}
.footer .office strong{color:#fff;font-size:8.5px}
.footer .socials{position:absolute;left:843px;top:78px;display:flex;gap:5px}
.footer .socials span{width:17px;height:17px;border-radius:50%;background:#777}
</style>
</head>
<body>

<header>
  <div class="abs topbar">
    <span class="abs welcome">Welcome to &nbsp;VONTAREX.</span>
    <span class="abs hotline">Hotline Support - 555-204-1187</span>
  </div>

  <div class="abs brand"><span class="dot"></span><span class="name">VONTAREX</span></div>

  <div class="abs social-head" aria-label="Social links"><span></span><span></span><span></span><span></span></div>

  <div class="abs search">Site Search
    <svg width="12" height="12" viewBox="0 0 12 12"><circle cx="5" cy="5" r="3.6" fill="none" stroke="#aaa" stroke-width="1.3"/><line x1="7.6" y1="7.6" x2="11" y2="11" stroke="#aaa" stroke-width="1.5"/></svg>
  </div>

  <nav class="abs nav">
    <span style="left:0">HOME</span><i style="left:37px"></i>
    <span class="active" style="left:54px">SERVICES</span><i style="left:112px"></i>
    <span style="left:121px">TEAM</span><i style="left:157px"></i>
    <span style="left:168px">FEATURES</span><i style="left:222px"></i>
    <span style="left:237px">BLOG</span><i style="left:271px"></i>
    <span style="left:283px">CONTACT US</span>
  </nav>
</header>

<section class="abs titleband">
  <h1>Services with 3 Column</h1>
  <div class="crumb">You are here &gt; Home &gt; Services</div>
  <div class="shade"></div>
</section>

<ul class="abs side">
  <li class="current" style="top:0">Overall VONTAREX</li>
  <hr style="top:25px">
  <li style="top:33px">Chromatography instrument and sotware training.</li>
  <hr style="top:60px">
  <li style="top:69px">Laboratory technicians</li>
  <hr style="top:96px">
  <li style="top:106px">Project Managers</li>
</ul>

<article class="abs intro">
  <h2>Overall VONTAREX</h2>
  <p>VONTAREX is focused on contractors for enhancing teams, but we also work in contract for hire, <b>temporary, and permanent</b> positions as well.</p>
  <p>Lorem Ipsum is simply dummy text of the printing and typesetting industry. Lorem Ipsum has been the industry's standard dummy text ever since the 1500s, when an <b>unknown printer</b> took a galley of type and scrambled it to make a type specimen book.</p>
</article>

<div class="abs feature-media" role="img" aria-label="Capsule filled with fruit under a magnifying glass"></div>

<div class="abs divider"></div>

<section>
  <div class="abs card active" style="left:259px;top:412px">
    <div class="media m-screen" role="img" aria-label="Medical data interface with heartbeat line"></div>
    <div class="cap"><h3>HEADING TITLE</h3><p>Lorem Ipsum Is Simple Dummy Text</p></div>
  </div>
  <div class="abs card" style="left:495px;top:412px">
    <div class="media m-tube" role="img" aria-label="Laboratory instrument tube glowing at the tip"></div>
    <div class="cap"><h3>HEADING TITLE</h3><p>Lorem Ipsum Is Simple Dummy Text</p></div>
  </div>
  <div class="abs card" style="left:733px;top:412px">
    <div class="media m-caps" role="img" aria-label="Blue capsules scattered on a dark surface"></div>
    <div class="cap"><h3>HEADING TITLE</h3><p>Lorem Ipsum Is Simple Dummy Text</p></div>
  </div>
  <div class="abs card" style="left:259px;top:616px">
    <div class="media m-tube" role="img" aria-label="Laboratory instrument tube glowing at the tip"></div>
    <div class="cap"><h3>HEADING TITLE</h3><p>Lorem Ipsum Is Simple Dummy Text</p></div>
  </div>
  <div class="abs card" style="left:495px;top:616px">
    <div class="media m-caps" role="img" aria-label="Blue capsules scattered on a dark surface"></div>
    <div class="cap"><h3>HEADING TITLE</h3><p>Lorem Ipsum Is Simple Dummy Text</p></div>
  </div>
  <div class="abs card" style="left:733px;top:616px">
    <div class="media m-screen" role="img" aria-label="Medical data interface with heartbeat line"></div>
    <div class="cap"><h3>HEADING TITLE</h3><p>Lorem Ipsum Is Simple Dummy Text</p></div>
  </div>
</section>

<div class="abs pager" style="left:259px;width:27px">1</div>
<div class="abs pager" style="left:288px;width:27px">2</div>
<div class="abs pager" style="left:904px;width:58px">Page 1 of 2</div>

<footer class="abs footer">
  <span class="mark"></span>
  <h4 style="left:317px;top:47px">ABOUT VONTAREX</h4>
  <span class="uline" style="left:317px;top:65px;width:119px"></span>
  <div class="about">
    <p>Lorem Ipsum is simply dummy text of the printing and typesetting industry. Lorem Ipsum has been the industry's standard dummy text ever since the 1500s, when an unknown printer took a galley of type and scrambled it to make a type specimen book.</p>
    <p>Lorem Ipsum is simply dummy text of the printing and typesetting industry. Lorem Ipsum has been the industry's standard dummy text ever since the 1500s, when an unknown printer took</p>
  </div>

  <h4 style="left:611px;top:47px">OFFICE LOCATION</h4>
  <span class="uline" style="left:611px;top:65px;width:120px"></span>
  <div class="office">
    1420 Alder Crest Lane, Fairhaven, CA &nbsp;90210<br>
    Email: <a>contact_us@VONTAREX.com</a><br>
    Call: <strong>555-204-1187</strong>
  </div>

  <h4 style="left:843px;top:47px">SOCIAL LINKS</h4>
  <span class="uline" style="left:843px;top:65px;width:119px"></span>
  <div class="socials"><span></span><span></span><span></span><span></span></div>
</footer>

</body>
</html>
```